Business Cards for new orthopaedic surgery practice

My husband and I are starting our own orthopaedic surgery practice. We are looking for a business card that is uniform, but one will have my name/title and the other will have his. You can just create one design with my name on it for now. But when I choose your design as the winning design I will ask that you add another copy with his name/title.

We are looking for classy, simple, elite all in one. We like dark blues/a little gold/yellow. Something that goes with our logo. We want our logo incorporated. Here is all the info you need:
Business name: RV Spine & Vitality Center
Location: 38915 North Bramble Ave
Maple Harbor, FL 33990
Phone: 954-218-4630
Fax: 954-571-2846
Email: info@myrvspine.example

Names: Lucinda Ferrow, M.D.
Board Certified Hand and Upper Extremity Surgeon

Emeka Dlunga, M.D.
Board Certified Hip & Knee Replacement/General Orthopaedic Surgeon

Can decide what you want to put on the back. Maybe a slogan:
Steady in Care. Centered on You

I am just going to upload our logo. The only thing is if we select you as the winning design, the location, and phone numbers may change. We will need your help to update that once fully solidified.

Industry/Entity Type

Medical

Contact Information for Business Card

Colors
0054AA
0677BA
7BADD7
CADEEF
E8F1F8
0094D4
00A9DD
6FCCEA
C7EBF8
E9F6FB

Requirements
Must have
• class, appeal,
Should not have
• We want to air on the side of masculine if we are looking at masculine vs. feminine feel. But we still want it classy, sophisticated, and something we will love

```html
<!DOCTYPE html>
<html lang="en">
<head>
<meta charset="utf-8">
<title>RV Spine &amp; Vitality Center – Business Card</title>
<link rel="stylesheet" href="https://fonts.googleapis.com/css2?family=Cinzel:wght@600&family=Arimo:wght@400&display=swap">
<style>
  :root {
    --backdrop: #e4e4e4;
    --navy: #1c2a55;
    --navy-top: #27375f;
    --navy-soft: #3a4f82;
    --gold: #c9a45a;
    --paper: #ffffff;
  }
  html, body {
    margin: 0;
    width: 1200px;
    height: 1200px;
    overflow: hidden;
    background: var(--backdrop);
  }
  .canvas { position: relative; width: 1200px; height: 1200px; }
  .card { position: absolute; width: 688px; height: 392px; overflow: hidden; }
  .card-front { left: 267px; top: 159px; background: var(--paper); }
  .card-back {
    left: 262px; top: 653px;
    background: linear-gradient(180deg, var(--navy-top) 0%, var(--navy) 100%);
  }

  .brand {
    position: absolute; left: 0; right: 0; top: 0; height: 229px;
    display: flex; align-items: center; justify-content: center; gap: 14px;
  }
  .brand-dot {
    width: 34px; height: 34px; border-radius: 50%;
    border: 3px solid var(--gold); box-sizing: border-box;
  }
  .brand-name {
    font-family: "Cinzel", serif; font-weight: 600; font-size: 26px;
    color: var(--navy); letter-spacing: 1px;
  }

  .gold-rule { position: absolute; left: 0; right: 0; top: 229px; height: 6px; background: var(--gold); }
  .info-band { position: absolute; left: 0; right: 0; top: 235px; bottom: 0; background: var(--navy); }

  .identity {
    position: absolute; right: 327px; top: 259px; text-align: right;
    font-family: "Arimo", sans-serif; color: #fff;
  }
  .doctor-name {
    font-family: "Cinzel", serif; font-weight: 600; font-size: 25px;
    color: var(--gold); line-height: 30px; margin: 0 0 1px; white-space: nowrap;
  }
  .doctor-title { font-size: 16px; line-height: 20px; margin: 0; }
  .address { font-size: 16.5px; line-height: 21px; margin: 4px 0 0; }

  .divider { position: absolute; left: 376px; top: 261px; width: 1px; height: 116px; background: #6d7898; }

  .contacts {
    position: absolute; left: 400px; top: 275px; margin: 0; padding: 0;
    list-style: none; font-family: "Arimo", sans-serif; font-size: 16.5px; color: #fff;
  }
  .contacts li { display: flex; align-items: center; height: 20.7px; }
  .contacts svg { width: 13px; height: 13px; margin-right: 10px; fill: var(--gold); }

  .back-name {
    position: absolute; left: 0; right: 0; top: 140px; text-align: center;
    font-family: "Cinzel", serif; font-weight: 600; font-size: 40px;
    color: var(--navy-soft); letter-spacing: 2px;
  }
  .slogan {
    position: absolute; left: 0; right: 0; top: 335px; text-align: center;
    font-family: "Arimo", sans-serif; font-size: 16.5px; letter-spacing: 3.2px;
    color: var(--gold); text-transform: uppercase;
  }
</style>
</head>
<body>
<main class="canvas">
  <section class="card card-front">
    <div class="brand">
      <span class="brand-dot"></span>
      <span class="brand-name">RV Spine &amp; Vitality Center</span>
    </div>
    <div class="gold-rule"></div>
    <div class="info-band"></div>

    <div class="identity">
      <p class="doctor-name">LUCINDA FERROW, M.D.</p>
      <p class="doctor-title">Board Certified Hand and</p>
      <p class="doctor-title">Upper Extremity Surgeon</p>
      <p class="address">38915 North Bramble Ave<br>Maple Harbor, FL 33990</p>
    </div>

    <div class="divider"></div>

    <ul class="contacts">
      <li>
        <svg viewBox="0 0 16 16"><path d="M3 1l3 3-1.5 2c1 2 3 4 5 5l2-1.5 3 3-2 2C6 14 2 10 1 3z"/></svg>
        954-218-4630
      </li>
      <li>
        <svg viewBox="0 0 16 16"><rect x="4" y="1" width="8" height="5"/><rect x="1" y="7" width="14" height="6" rx="1"/><rect x="4" y="13" width="8" height="2"/></svg>
        954-571-2846
      </li>
      <li>
        <svg viewBox="0 0 16 16"><path d="M1 3h14v10H1z M2 4l6 5 6-5" fill="none" stroke="#c9a45a" stroke-width="1.6"/></svg>
        info@myrvspine.example
      </li>
      <li>
        <svg viewBox="0 0 16 16"><circle cx="8" cy="8" r="6.5" fill="none" stroke="#c9a45a" stroke-width="1.6"/><path d="M5 4c2 1 1 3 3 3s1 3 3 3l-1 3c-3-1-2-3-4-4S4 6 5 4z"/></svg>
        www.myrvspine.example
      </li>
    </ul>
  </section>

  <section class="card card-back">
    <div class="back-name">RV Spine &amp; Vitality Center</div>
    <div class="slogan">Steady in Care. Centered on You</div>
  </section>
</main>
</body>
</html>
```